BRIM Outreach Partners Business Card Rebrand

Hello Designers! We are looking for help designing our new business card to go in conjunction with our company rebrand. Unfortunately, we have an event mid June that requires we get these printed ASAP (before our new website is launched.) We have a mostly complete Brand Book which I have uploaded to this request for your reference to company information, style, fonts. I've also enclosed our logo file in .eps & .jpg. Attached is a sample business card my boss liked but said was "too simple." I made it in Canva and do not profess to be a designer. NOT FOR DESIGN REFERENCE, ONLY FOR CONTEXT Here is what our old website looks like: https://brimoutreachpartners.com/.

```html
<!DOCTYPE html>
<html lang="en">
<head>
<meta charset="utf-8">
<title>BRIM Outreach Partners – Business Card</title>
<link href="https://fonts.googleapis.com/css2?family=Montserrat:wght@600;700&family=Open+Sans:wght@400;600&display=swap" rel="stylesheet">
<style>
  :root {
    --backdrop: #3b3b3b;
    --card: #1a1a1a;
    --card-back: #161616;
    --brand-blue: #4db3e6;
    --ink-white: #f2f2f2;
    --ink-soft: #d6d6d6;
    --ink-grey: #9a9a9a;
    --emboss: #0c0c0c;
    --divider: #4a4a4a;
  }
  * { box-sizing: border-box; margin: 0; padding: 0; }
  html, body {
    width: 1200px; height: 801px; overflow: hidden;
    background: var(--backdrop);
  }
  .stage {
    position: relative; width: 1200px; height: 801px;
    display: flex; align-items: center; justify-content: center; gap: 44px;
  }
  .card {
    position: relative; width: 525px; height: 300px;
    background: var(--card);
    border-bottom: 3px solid var(--brand-blue);
    border-left: 2px solid var(--brand-blue);
    box-shadow: 0 14px 30px rgba(0,0,0,.45);
    overflow: hidden;
  }
  .card--back { background: var(--card-back); }

  /* front */
  .brand {
    position: absolute; left: 70px; top: 62px;
    display: flex; align-items: center; gap: 18px;
  }
  .brand__dot {
    width: 74px; height: 74px; border-radius: 50%;
    background: var(--brand-blue); flex: none;
  }
  .brand__name {
    font-family: "Montserrat", sans-serif; font-weight: 700;
    font-size: 30px; line-height: 1.02; letter-spacing: .5px;
    color: var(--ink-white); text-transform: uppercase;
  }
  .holder {
    position: absolute; left: 70px; top: 190px; width: 200px;
  }
  .holder__name {
    font-family: "Montserrat", sans-serif; font-weight: 700;
    font-size: 17px; letter-spacing: .6px; color: var(--brand-blue);
    text-transform: uppercase;
  }
  .holder__title {
    font-family: "Open Sans", sans-serif; font-size: 13px;
    color: var(--ink-soft); margin-top: 3px;
  }
  .divider {
    position: absolute; left: 272px; top: 172px;
    width: 1px; height: 86px; background: var(--divider);
  }
  .contacts {
    position: absolute; left: 290px; top: 172px; list-style: none;
    font-family: "Open Sans", sans-serif; font-size: 12.5px; color: var(--ink-soft);
  }
  .contacts li { display: flex; align-items: center; gap: 8px; height: 21.5px; }
  .contacts svg { width: 11px; height: 11px; fill: var(--brand-blue); flex: none; }

  /* back */
  .back-brand {
    position: absolute; left: 110px; top: 100px;
    display: flex; align-items: center; gap: 22px;
  }
  .back-brand__dot {
    width: 96px; height: 96px; border-radius: 50%;
    background: var(--emboss); flex: none;
  }
  .back-brand__name {
    font-family: "Montserrat", sans-serif; font-weight: 700;
    font-size: 34px; line-height: 1.02; letter-spacing: .5px;
    color: var(--ink-grey); text-transform: uppercase;
  }
</style>
</head>
<body>
<main class="stage">
  <section class="card card--front">
    <div class="brand">
      <span class="brand__dot"></span>
      <p class="brand__name">BRIM Outreach<br>Partners</p>
    </div>
    <div class="holder">
      <p class="holder__name">Daniel Reyes-Holt</p>
      <p class="holder__title">Managing Partner</p>
    </div>
    <span class="divider"></span>
    <ul class="contacts">
      <li><svg viewBox="0 0 24 24"><path d="M6.6 10.8a15 15 0 0 0 6.6 6.6l2.2-2.2a1 1 0 0 1 1-.25 11.4 11.4 0 0 0 3.6.57 1 1 0 0 1 1 1V20a1 1 0 0 1-1 1A17 17 0 0 1 3 4a1 1 0 0 1 1-1h3.5a1 1 0 0 1 1 1c0 1.25.2 2.45.57 3.57a1 1 0 0 1-.25 1z"/></svg>+945-555-0147</li>
      <li><svg viewBox="0 0 24 24"><path d="M12 2a7 7 0 0 0-7 7c0 5.2 7 13 7 13s7-7.8 7-13a7 7 0 0 0-7-7zm0 9.5A2.5 2.5 0 1 1 12 6.5a2.5 2.5 0 0 1 0 5z"/></svg>Denver, CO based (Mountain Time)</li>
      <li><svg viewBox="0 0 24 24"><path d="M2 5h20v14H2zm2 2v.5l8 5 8-5V7l-8 5z"/></svg>daniel@brimoutreachpartners.com</li>
      <li><svg viewBox="0 0 24 24"><path d="M12 2a10 10 0 1 0 0 20 10 10 0 0 0 0-20zm6.9 9h-3a15 15 0 0 0-1.2-5.6A8 8 0 0 1 18.9 11zM12 4c.9 1.2 1.8 3.6 1.9 7h-3.8c.1-3.4 1-5.8 1.9-7zM9.3 5.4A15 15 0 0 0 8.1 11h-3a8 8 0 0 1 4.2-5.6zM5.1 13h3a15 15 0 0 0 1.2 5.6A8 8 0 0 1 5.1 13zM12 20c-.9-1.2-1.8-3.6-1.9-7h3.8c-.1 3.4-1 5.8-1.9 7zm2.7-1.4a15 15 0 0 0 1.2-5.6h3a8 8 0 0 1-4.2 5.6z"/></svg>brimoutreachpartners.com</li>
    </ul>
  </section>

  <section class="card card--back">
    <div class="back-brand">
      <span class="back-brand__dot"></span>
      <p class="back-brand__name">BRIM Outreach<br>Partners</p>
    </div>
  </section>
</main>
</body>
</html>
```